Redesign This Psychology Website

We would like a slight redesign of this successful psychology (relationship counselling) website:

www.TheWillowNook.com.au

We are updating the website, and we'd like a slight refresh of the design and style.

Please keep to very similar colours, and use the same logo. We're looking for around 10 page templates, however the main one is the home page.

Keep in mind, this website already converts quite well, so we want a new, fresh design in keeping with this one. Please don't bother designing something too extremely different.

thanks :)

Target Market(s)

couples who are looking for relationship counselling. Men and women, 25 - 70, across Australia

Industry/Entity Type

Psychology

Number of Pages Required

5+ page

Font styles to use
Sans Serif

Colors
87cfc6
b7a5cd
ec1f27
ffffff
cee9f5

Requirements
Must have
• a similar look to the current design, just looking for a slight refresh.
• Search bar
• Areas for lots of photos
• same logo
• lots of content areas
Nice to have
• great content areas, where we can display a lot of content and our areas.
Should not have
• no colors like orange, etc.
• should not have a totally different feel.

```html
<!DOCTYPE html>
<html lang="en">
<head>
<meta charset="utf-8">
<title>The Willow Nook – Relationship Counselling</title>
<link rel="stylesheet" href="https://fonts.googleapis.com/css2?family=Dosis:wght@500;600;700&family=Open+Sans:ital,wght@0,400;1,400&display=swap">
<style>
  :root {
    --teal: #1b7f8f;
    --teal-light: #5fc4d2;
    --red: #e8202a;
    --topbar: #555555;
    --text: #2b2b2b;
    --panel: #ebebeb;
    --white: #ffffff;
    --input-border: #cfcfcf;
  }
  * { box-sizing: border-box; margin: 0; padding: 0; }
  html, body { width: 1008px; height: 1200px; overflow: hidden; background: var(--white); }
  body { position: relative; font-family: "Open Sans", Arial, sans-serif; color: var(--text); }

  .topbar { position: absolute; left: 0; top: 0; width: 1008px; height: 21px; background: var(--topbar); }
  .topbar-links { position: absolute; left: 464px; top: 0; display: flex; gap: 16px; list-style: none; line-height: 21px; font-size: 9.6px; text-transform: uppercase; color: var(--white); }
  .topbar-links .highlight { color: var(--red); }

  .site-header { position: absolute; left: 0; top: 21px; width: 1008px; height: 95px; background: linear-gradient(90deg, #f1f2ee, #f6f6f3 50%, #eef0ea); }
  .brand-dot { position: absolute; left: 133px; top: 14px; width: 56px; height: 56px; border-radius: 50%; background: var(--teal); }
  .brand-name { position: absolute; left: 196px; top: 24px; font-family: "Dosis", sans-serif; font-weight: 500; font-size: 32px; line-height: 36px; color: var(--teal); white-space: nowrap; }
  .brand-tagline { position: absolute; left: 197px; top: 73px; font-family: "Dosis", sans-serif; font-weight: 500; font-size: 10px; color: var(--teal); }

  .hero { position: absolute; left: 0; top: 116px; width: 1008px; height: 410px;
    background:
      radial-gradient(ellipse 210px 150px at 60px 330px, rgba(232,80,80,0.95), rgba(232,80,80,0) 100%),
      radial-gradient(ellipse 330px 260px at 880px 240px, rgba(28,36,56,0.95) 40%, rgba(28,36,56,0) 100%),
      radial-gradient(ellipse 170px 130px at 560px 200px, rgba(214,160,130,0.9), rgba(214,160,130,0) 100%),
      radial-gradient(ellipse 200px 90px at 440px 320px, rgba(236,214,190,0.9), rgba(236,214,190,0) 100%),
      radial-gradient(ellipse 160px 100px at 330px 100px, rgba(230,200,180,0.7), rgba(230,200,180,0) 100%),
      linear-gradient(165deg, #c6dd98 0%, #8dbb52 35%, #5d9631 65%, #6fa03f 100%); }

  .main-nav { position: absolute; left: 0; top: 526px; width: 1008px; height: 72px; background: linear-gradient(#ffffff, #eef1f2); border-bottom: 1px solid #d7e6ea; box-shadow: 0 3px 6px rgba(95,196,210,0.25); }
  .main-nav ul { position: absolute; left: 132px; top: 0; display: flex; list-style: none; height: 72px; }
  .main-nav li { display: flex; align-items: center; justify-content: center; text-align: center; height: 72px; width: 123px; font-family: "Dosis", sans-serif; font-weight: 700; font-size: 10.5px; line-height: 1.25; color: var(--teal); text-transform: uppercase; border-right: 1px solid #d5dde0; }
  .main-nav li:last-child { border-right: none; width: 132px; }

  .services { position: absolute; left: 0; top: 640px; width: 1008px; }
  .service { position: absolute; width: 180px; text-align: center; }
  .service h2 { font-family: "Dosis", sans-serif; font-weight: 600; font-size: 13px; line-height: 16px; color: var(--red); text-transform: uppercase; }
  .service-photo { width: 126px; height: 126px; margin: 18px auto 0; border-radius: 50%; border: 2px solid var(--teal-light); }
  .service p { margin-top: 12px; font-size: 8.8px; line-height: 12px; color: var(--text); white-space: nowrap; }
  .s1 { left: 124px; } .s2 { left: 313px; } .s3 { left: 502px; } .s4 { left: 691px; }
  .s1 .service-photo { background:
      radial-gradient(ellipse 28px 50px at 42px 70px, rgba(170,170,170,0.9), rgba(170,170,170,0) 100%),
      radial-gradient(ellipse 28px 50px at 82px 72px, rgba(190,185,180,0.9), rgba(190,185,180,0) 100%),
      radial-gradient(circle 14px at 50px 30px, rgba(200,160,130,0.9), rgba(200,160,130,0)),
      radial-gradient(circle 13px at 82px 38px, rgba(200,160,130,0.9), rgba(200,160,130,0)),
      linear-gradient(#fafafa, #e4e4e4); }
  .s2 .service-photo { background:
      radial-gradient(ellipse 60px 30px at 70px 100px, rgba(255,255,255,0.95), rgba(255,255,255,0)),
      radial-gradient(circle 18px at 40px 40px, rgba(225,220,215,0.95), rgba(225,220,215,0)),
      radial-gradient(circle 18px at 82px 58px, rgba(205,150,120,0.9), rgba(205,150,120,0)),
      linear-gradient(#f6f3ef, #e7ddd3); }
  .s3 .service-photo { background:
      radial-gradient(ellipse 44px 34px at 61px 108px, rgba(255,255,255,1), rgba(255,255,255,0)),
      radial-gradient(ellipse 22px 30px at 61px 46px, rgba(200,160,140,0.95), rgba(200,160,140,0)),
      radial-gradient(ellipse 26px 14px at 61px 18px, rgba(150,150,150,0.9), rgba(150,150,150,0)),
      linear-gradient(#f7f7f7, #e6e6e6); }
  .s4 .service-photo { background:
      radial-gradient(ellipse 46px 60px at 58px 70px, rgba(160,70,40,0.95), rgba(160,70,40,0)),
      radial-gradient(ellipse 18px 24px at 60px 46px, rgba(235,200,180,0.95), rgba(235,200,180,0)),
      radial-gradient(circle 10px at 84px 64px, rgba(240,200,40,0.95), rgba(240,200,40,0)),
      radial-gradient(ellipse 40px 20px at 60px 112px, rgba(225,170,160,0.9), rgba(225,170,160,0)),
      linear-gradient(#f5f2f0, #ece4e0); }

  .about-panel { position: absolute; left: 0; top: 916px; width: 1008px; height: 262px; background: var(--panel); }
  .about { position: absolute; left: 138px; top: 28px; width: 480px; }
  .about h1 { font-family: "Dosis", sans-serif; font-weight: 600; font-size: 17px; line-height: 20px; color: var(--teal); text-transform: uppercase; white-space: nowrap; }
  .about p { margin-top: 13px; font-size: 10px; line-height: 13.2px; text-align: justify; }
  .about h1 + p { margin-top: 8px; }

  .finder { position: absolute; left: 662px; top: 28px; width: 172px; }
  .finder h2 { font-family: "Dosis", sans-serif; font-weight: 600; font-size: 15.5px; line-height: 18px; color: var(--teal); text-align: center; text-transform: uppercase; }
  .finder label { display: block; margin: 17px 0 3px 5px; font-size: 9px; font-style: italic; color: var(--teal); }
  .field { display: block; width: 172px; height: 21px; padding-left: 6px; line-height: 19px; font-size: 8.5px; font-style: italic; color: #9a9a9a; background: var(--white); border: 1px solid var(--input-border); border-top-color: #bdbdbd; }
  .field + .field { margin-top: 19px; }
  .field.postcode { margin-top: 27px; }
  .search-btn { display: block; width: 68px; height: 19px; margin: 14px auto 0; background: var(--red); color: var(--white); font-family: "Dosis", sans-serif; font-weight: 600; font-size: 10px; text-align: center; line-height: 19px; }
</style>
</head>
<body>
  <div class="topbar">
    <ul class="topbar-links">
      <li class="highlight">Join our associate program</li>
      <li>Relationship counselling</li>
      <li>Marriage counselling</li>
    </ul>
  </div>

  <header class="site-header">
    <span class="brand-dot"></span>
    <span class="brand-name">The Willow Nook</span>
    <div class="brand-tagline">helping you create loving relationships</div>
  </header>

  <div class="hero" role="img" aria-label="Photo of a couple lying in green grass, foreheads touching; she wears a red top, he a navy t-shirt"></div>

  <nav class="main-nav">
    <ul>
      <li>Councelling<br>types</li>
      <li>Relationship<br>counselling<br>locations</li>
      <li>Sex therapy<br>locations</li>
      <li>Quizzes</li>
      <li>FAQ's</li>
      <li>Contact</li>
    </ul>
  </nav>

  <section class="services">
    <article class="service s1">
      <h2>Relationship<br>counselling</h2>
      <div class="service-photo" role="img" aria-label="Photo of a smiling couple in grey knitwear"></div>
      <p>Communication, Recovering from an<br>affair, Loss of intimacy &amp; love, Power<br>battles, Feeling like friends, not lovers</p>
    </article>
    <article class="service s2">
      <h2>Sex therapy<br>counselling</h2>
      <div class="service-photo" role="img" aria-label="Photo of an older couple relaxing in bed"></div>
      <p>Low libido , Erectile difficulties,<br>Premature ejaculation, Differing libidos,<br>Porn addiction, Keeping sex exciting</p>
    </article>
    <article class="service s3">
      <h2>Anger management<br>counselling</h2>
      <div class="service-photo" role="img" aria-label="Photo of a frowning grey-haired man in a white shirt"></div>
      <p>Managing angry outbursts, expressing<br>your anger in healthy ways</p>
    </article>
    <article class="service s4">
      <h2>Narcissism<br>counselling</h2>
      <div class="service-photo" role="img" aria-label="Photo of a red-haired woman holding a yellow flower"></div>
      <p>Managing narcissistic, superior, entitled,<br>arrogant and lack of empathy tendencies<br>in you or your partner</p>
    </article>
  </section>

  <section class="about-panel">
    <div class="about">
      <h1>We specialise in relationship &amp; marriage counselling</h1>
      <p>At the Willow Nook, we are a group of PSYCHOLOGISTS, Australia wide who are passionate about relationships and helping you with yours.</p>
      <p>Our vision is to provide the most highly regarded and comprehensive marriage counselling and relationship counselling, and sex therapy in Australia, at reasonable and affordable rates.</p>
      <p>When we are experiencing relationship and marriage problems, there can be a lot of pain and confusion, and it can often be difficult to cope with the other areas of our lives when we are struggling with problems with our partner.</p>
      <p>We are not taught about relationships and how to have a good one in our schools, so most of us are doing the best we know how, but lack the knowledge on how to create a better relationship.</p>
    </div>
    <div class="finder">
      <h2>Find our psychologist<br>near you</h2>
      <label>Type of Counselling</label>
      <span class="field">Please select</span>
      <span class="field">Location</span>
      <span class="field postcode">Postcode</span>
      <span class="search-btn">SEARCH</span>
    </div>
  </section>
</body>
</html>
```